Brisk Lumo Entertainment

I need a web design for my Business for better online promotions and services.. The name of my company is Brisk Lumo its a entertainment company music, events, networking and so on.. What I do is help artist create and finish projects such as mix tapes, music videos, and book performances in order to create a platform and i also offer representation to help grow there brands or business... I also work with and help develop independent artists!!!

Target Market(s)

Hip hop and R&B industry

Industry/Entity Type

Entertainment Industry

Number of Pages Required

1 page

Requirements
Must have
• Must display My previous and upcoming work i want people to see the quality I provide in my service.. I have more videos that I want to upload on there to show more work.... I would like to bring all the separate promotions and campaigns that I previously had and currently have all one platform for everybody to see and to find more easily instead having everything so spread out..
Nice to have
• Creativity thats going to compliment my work and quality..

```html
<!DOCTYPE html>
<html lang="en">
<head>
<meta charset="utf-8">
<title>Brisk Lumo Entertainment – Work</title>
<link href="https://fonts.googleapis.com/css2?family=Ubuntu:wght@400;500;700&display=swap" rel="stylesheet">
<style>
:root{
  --red:#d3101c;
  --ink:#2a2a2a;
  --white:#ffffff;
  --muted:#8a8a8a;
  --band:#7d7e82;
  --band-dark:#5d5e62;
  --card-border:#1e1e1e;
}
*{box-sizing:border-box;margin:0;padding:0}
html,body{width:1200px;height:800px;overflow:hidden;background:var(--white);font-family:'Ubuntu',sans-serif}
.page{position:relative;width:1200px;height:800px}
.section-title{font-size:30px;font-weight:500;text-align:center;letter-spacing:.5px}
.section-title .accent{color:var(--red)}
.upcoming{position:absolute;left:0;top:0;width:1200px;height:437px;background:var(--white)}
.upcoming .section-title{position:absolute;top:8px;width:100%;color:var(--ink)}
.work-grid{position:absolute;top:76px;left:185px;display:flex;gap:22px}
.work-tile{position:relative;width:262px;height:262px;overflow:hidden}
.work-tile .art{position:absolute;inset:0}
.tile-one .art{background:radial-gradient(circle at 50% 45%,#5aa845 0%,#1f4a22 55%,#0d1f10 100%)}
.tile-two .art{background:radial-gradient(circle at 45% 65%,#3a9ac0 0%,#8b8b8b 45%,#2d2d2d 100%)}
.tile-three .art{background:linear-gradient(160deg,#2a2a2a 0%,#8d8d8d 55%,#cfcfcf 100%)}
.tile-caption{position:absolute;left:0;right:0;bottom:0;height:26px;background:rgba(0,0,0,.55);color:var(--white);font-size:12px;display:flex;align-items:center;justify-content:center}
.tile-caption .play{position:absolute;right:10px;top:5px}
.view-all{position:absolute;top:372px;left:528px;width:143px;height:27px;background:var(--red);color:var(--white);font-size:11px;font-weight:700;display:flex;align-items:center;justify-content:center;letter-spacing:.3px}
.latest{position:absolute;left:0;top:437px;width:1200px;height:363px;background:radial-gradient(ellipse at 65% 25%,#a9aaae 0%,var(--band) 45%,var(--band-dark) 100%)}
.latest .section-title{position:absolute;top:22px;width:100%;color:var(--white)}
.release-list{position:absolute;top:83px;left:185px;display:grid;grid-template-columns:404px 404px;column-gap:22px;row-gap:15px}
.release{height:76px;background:var(--white);border:3px solid var(--card-border);display:flex;align-items:center;padding:0 14px}
.release .calendar{flex:none}
.release .date{margin-left:22px;width:70px;color:var(--muted);font-size:12px;line-height:14px}
.release .thumb{width:38px;height:38px;flex:none;margin-left:8px}
.thumb-teal{background:linear-gradient(180deg,#d9e6e8,#3ea6a8)}
.thumb-gold{background:linear-gradient(180deg,#2d2d1a,#c7b23a)}
.release .title{flex:1;margin-left:20px;font-size:11px;color:var(--ink);white-space:nowrap}
.release .play{flex:none}
</style>
</head>
<body>
<main class="page">
  <section class="upcoming">
    <h2 class="section-title"><span class="accent">UPCOMING</span> WORK</h2>
    <div class="work-grid">
      <article class="work-tile tile-one">
        <div class="art" role="img" aria-label="Mixtape cover art for Rico Vale The Regent in green jungle tones"></div>
        <div class="tile-caption">Rico Vale The Regent
          <svg class="play" width="16" height="16" viewBox="0 0 16 16"><circle cx="8" cy="8" r="7" fill="none" stroke="#fff" stroke-width="1.3"/><path d="M6.5 5v6l4.5-3z" fill="#fff"/></svg>
        </div>
      </article>
      <article class="work-tile tile-two">
        <div class="art" role="img" aria-label="DJ hand on a turntable with a blue record"></div>
        <div class="tile-caption">HIP HOP
          <svg class="play" width="16" height="16" viewBox="0 0 16 16"><circle cx="8" cy="8" r="7" fill="none" stroke="#fff" stroke-width="1.3"/><path d="M6.5 5v6l4.5-3z" fill="#fff"/></svg>
        </div>
      </article>
      <article class="work-tile tile-three">
        <div class="art" role="img" aria-label="Black and white photo of a studio mixing console"></div>
        <div class="tile-caption">R&amp;B
          <svg class="play" width="16" height="16" viewBox="0 0 16 16"><circle cx="8" cy="8" r="7" fill="none" stroke="#fff" stroke-width="1.3"/><path d="M6.5 5v6l4.5-3z" fill="#fff"/></svg>
        </div>
      </article>
    </div>
    <a class="view-all">VIEW ALL</a>
  </section>

  <section class="latest" role="img" aria-label="Grey backdrop photo of a studio microphone">
    <h2 class="section-title"><span class="accent">LATEST</span> WORK</h2>
    <div class="release-list">
      <article class="release">
        <svg class="calendar" width="30" height="30" viewBox="0 0 30 30"><rect x="2" y="5" width="26" height="23" fill="none" stroke="#222" stroke-width="2.5"/><rect x="2" y="5" width="26" height="6" fill="#222"/><path d="M8 2v6M22 2v6" stroke="#222" stroke-width="2.5"/><path d="M8 15h3M14 15h3M20 15h3M8 20h3M14 20h3M20 20h3M8 24h3M14 24h3" stroke="#222" stroke-width="2.5"/></svg>
        <div class="date">20 Jan<br>2017</div>
        <div class="thumb thumb-teal" role="img" aria-label="Artist photo thumbnail"></div>
        <div class="title">Tomas Keller - Trance</div>
        <svg class="play" width="18" height="18" viewBox="0 0 18 18"><circle cx="9" cy="9" r="7.5" fill="none" stroke="#222" stroke-width="1.5"/><path d="M7.3 5.8v6.4l5-3.2z" fill="#222"/></svg>
      </article>
      <article class="release">
        <svg class="calendar" width="30" height="30" viewBox="0 0 30 30"><rect x="2" y="5" width="26" height="23" fill="none" stroke="#222" stroke-width="2.5"/><rect x="2" y="5" width="26" height="6" fill="#222"/><path d="M8 2v6M22 2v6" stroke="#222" stroke-width="2.5"/><path d="M8 15h3M14 15h3M20 15h3M8 20h3M14 20h3M20 20h3M8 24h3M14 24h3" stroke="#222" stroke-width="2.5"/></svg>
        <div class="date">20 Jan<br>2017</div>
        <div class="thumb thumb-teal" role="img" aria-label="Artist photo thumbnail"></div>
        <div class="title">Tomas Keller - Trance</div>
        <svg class="play" width="18" height="18" viewBox="0 0 18 18"><circle cx="9" cy="9" r="7.5" fill="none" stroke="#222" stroke-width="1.5"/><path d="M7.3 5.8v6.4l5-3.2z" fill="#222"/></svg>
      </article>
      <article class="release">
        <svg class="calendar" width="30" height="30" viewBox="0 0 30 30"><rect x="2" y="5" width="26" height="23" fill="none" stroke="#222" stroke-width="2.5"/><rect x="2" y="5" width="26" height="6" fill="#222"/><path d="M8 2v6M22 2v6" stroke="#222" stroke-width="2.5"/><path d="M8 15h3M14 15h3M20 15h3M8 20h3M14 20h3M20 20h3M8 24h3M14 24h3" stroke="#222" stroke-width="2.5"/></svg>
        <div class="date">20 Jan<br>2017</div>
        <div class="thumb thumb-gold" role="img" aria-label="Group cover thumbnail"></div>
        <div class="title">Hip Hop Group - Deep Cut</div>
        <svg class="play" width="18" height="18" viewBox="0 0 18 18"><circle cx="9" cy="9" r="7.5" fill="none" stroke="#222" stroke-width="1.5"/><path d="M7.3 5.8v6.4l5-3.2z" fill="#222"/></svg>
      </article>
      <article class="release">
        <svg class="calendar" width="30" height="30" viewBox="0 0 30 30"><rect x="2" y="5" width="26" height="23" fill="none" stroke="#222" stroke-width="2.5"/><rect x="2" y="5" width="26" height="6" fill="#222"/><path d="M8 2v6M22 2v6" stroke="#222" stroke-width="2.5"/><path d="M8 15h3M14 15h3M20 15h3M8 20h3M14 20h3M20 20h3M8 24h3M14 24h3" stroke="#222" stroke-width="2.5"/></svg>
        <div class="date">20 Jan<br>2017</div>
        <div class="thumb thumb-teal" role="img" aria-label="Artist photo thumbnail"></div>
        <div class="title">Tomas Keller - Trance</div>
        <svg class="play" width="18" height="18" viewBox="0 0 18 18"><circle cx="9" cy="9" r="7.5" fill="none" stroke="#222" stroke-width="1.5"/><path d="M7.3 5.8v6.4l5-3.2z" fill="#222"/></svg>
      </article>
    </div>
  </section>
</main>
</body>
</html>
```